Brightleaf Plots needs a business card

I need a business card using the logo that was selected. I would like the front to have the words "local", "sustainable", "healthy", and "elegant". I would also like the front to have my name on the card as Marisa Holcombe.

The back of the card can list what I do: Container Design & Installation, Vegetable Garden Design & Installation.
It can also list my contact information: Mobile Phone 914-583-6021, and email brightleafplots27@mailtrove.net

```html
<!DOCTYPE html>
<html lang="en">
<head>
<meta charset="utf-8">
<title>Brightleaf Plots – Business Card</title>
<link rel="stylesheet" href="https://fonts.googleapis.com/css2?family=Raleway:wght@300;400;600&display=swap">
<style>
  :root {
    --leaf-green: #a3cd3b;
    --leaf-green-soft: #b6d865;
    --card-white: #ffffff;
    --stage: #eeeae2;
    --ink-white: #ffffff;
  }
  * { box-sizing: border-box; margin: 0; padding: 0; }
  html, body {
    width: 1200px; height: 1000px; overflow: hidden;
    background: var(--stage);
    font-family: "Raleway", Arial, sans-serif;
  }
  .stage {
    position: relative; width: 1200px; height: 1000px;
  }
  .card {
    position: absolute; left: 250px; width: 700px; height: 400px;
    overflow: hidden;
    box-shadow: 0 6px 18px rgba(0,0,0,0.18);
  }
  .card--front { top: 60px; background: var(--card-white); }
  .card--back  { top: 540px; background: var(--leaf-green); }

  /* front */
  .brand {
    position: absolute; left: 40px; top: 70px; width: 290px;
    display: flex; flex-direction: column; align-items: center; gap: 22px;
  }
  .brand__dot {
    width: 120px; height: 120px; border-radius: 50%;
    background: var(--leaf-green);
  }
  .brand__name {
    font-size: 34px; font-weight: 400; color: var(--leaf-green);
    white-space: nowrap;
  }
  .divider {
    position: absolute; left: 357px; top: 68px; width: 3px; height: 225px;
    background: var(--leaf-green);
  }
  .contact {
    position: absolute; left: 385px; top: 108px; color: var(--leaf-green);
  }
  .contact__name {
    font-size: 27px; font-weight: 600; letter-spacing: 1.5px;
    margin-bottom: 26px;
  }
  .contact__label, .contact__value {
    font-size: 17px; font-weight: 400; line-height: 1.35;
  }
  .contact__value { margin-bottom: 6px; }
  .wave {
    position: absolute; left: 0; bottom: 0; width: 700px; height: 120px;
  }
  .tagline {
    position: absolute; left: 0; right: 0; bottom: 14px;
    text-align: center; color: var(--ink-white);
    font-size: 18px; font-weight: 400; letter-spacing: 4.2px;
  }

  /* back */
  .back-mark {
    position: absolute; left: 30px; top: 20px;
    width: 330px; height: 330px; border-radius: 50%;
    background: var(--leaf-green-soft);
  }
  .services {
    position: absolute; right: 40px; bottom: 60px;
    list-style: none; text-align: right; color: var(--ink-white);
    font-size: 22px; font-weight: 300; line-height: 1.6;
  }
</style>
</head>
<body>
<main class="stage">
  <section class="card card--front" aria-label="Business card front">
    <div class="brand">
      <span class="brand__dot"></span>
      <span class="brand__name">Brightleaf Plots</span>
    </div>
    <span class="divider"></span>
    <div class="contact">
      <p class="contact__name">MARISA HOLCOMBE</p>
      <p class="contact__label">Phone :</p>
      <p class="contact__value">914-583-6021</p>
      <p class="contact__label">Email :</p>
      <p class="contact__value">brightleafplots27@mailtrove.net</p>
    </div>
    <svg class="wave" viewBox="0 0 700 120" preserveAspectRatio="none" aria-hidden="true">
      <path d="M0,78 C120,92 220,70 340,40 C460,10 580,12 700,34 L700,120 L0,120 Z" fill="var(--leaf-green)"/>
    </svg>
    <p class="tagline">LOCAL, SUSTAINABLE, HEALTHY, AND ELEGANT</p>
  </section>

  <section class="card card--back" aria-label="Business card back">
    <span class="back-mark"></span>
    <ul class="services">
      <li>Container Design &amp; Installation</li>
      <li>Vegetable Garden Design &amp; Installation</li>
    </ul>
  </section>
</main>
</body>
</html>
```